Glint5Gate Photography Business Cards

We need a good general business card that we can hand to our clients. We will be doing embossed gloss cards.

Target Market(s)

Real estate / Business to business / professionals

```html
<!DOCTYPE html>
<html lang="en">
<head>
<meta charset="utf-8">
<title>Glint5Gate Photography – Business Cards</title>
<link rel="stylesheet" href="https://fonts.googleapis.com/css2?family=Open+Sans:wght@600;700&display=swap">
<style>
  :root {
    --backdrop: #4a4a4c;
    --navy-deep: #17194a;
    --navy-mid: #1a2a6e;
    --blue-glow: #1668ad;
    --ink-navy: #2a2760;
    --sky: #3aa4de;
    --paper: #f4f4f4;
    --white: #ffffff;
  }
  * { margin: 0; padding: 0; box-sizing: border-box; }
  html, body {
    width: 1200px;
    height: 1200px;
    overflow: hidden;
    background: var(--backdrop);
    font-family: "Open Sans", Arial, sans-serif;
  }
  .sheet {
    position: relative;
    width: 1200px;
    height: 1200px;
  }
  .card {
    position: absolute;
    left: 250px;
    width: 700px;
    height: 400px;
    box-shadow: 0 18px 40px rgba(0, 0, 0, 0.45);
    overflow: hidden;
  }
  .card-front {
    top: 150px;
    background: radial-gradient(circle at 50% 50%, var(--blue-glow) 0%, var(--navy-mid) 45%, var(--navy-deep) 85%);
    display: flex;
    align-items: center;
    justify-content: center;
  }
  .badge-ring {
    width: 270px;
    height: 270px;
    border: 4px solid var(--white);
    border-radius: 50%;
    display: flex;
    flex-direction: column;
    align-items: center;
    justify-content: center;
    color: var(--white);
    font-weight: 600;
    text-align: center;
  }
  .badge-name {
    font-size: 38px;
    line-height: 1.1;
  }
  .badge-sub {
    font-size: 20px;
    letter-spacing: 3px;
    margin-top: 8px;
  }
  .card-back {
    top: 650px;
    background: var(--paper);
    display: flex;
    flex-direction: column;
    align-items: center;
    justify-content: center;
    gap: 34px;
  }
  .wordmark {
    color: var(--ink-navy);
    font-weight: 700;
    text-align: center;
    line-height: 1;
  }
  .wordmark-name {
    font-size: 78px;
    letter-spacing: -1px;
  }
  .wordmark-sub {
    font-size: 30px;
    letter-spacing: 9px;
    margin-top: 10px;
  }
  .social-row {
    display: flex;
    gap: 26px;
    list-style: none;
  }
  .social-item {
    display: flex;
    align-items: center;
    gap: 8px;
    color: var(--sky);
    font-size: 15px;
    font-weight: 600;
  }
  .social-dot {
    width: 22px;
    height: 22px;
    border-radius: 50%;
    background: var(--sky);
  }
</style>
</head>
<body>
  <main class="sheet">
    <section class="card card-front" aria-label="Card front">
      <div class="badge-ring">
        <span class="badge-name">Glint5Gate</span>
        <span class="badge-sub">PHOTOGRAPHY</span>
      </div>
    </section>

    <section class="card card-back" aria-label="Card back">
      <div class="wordmark">
        <div class="wordmark-name">Glint5Gate</div>
        <div class="wordmark-sub">PHOTOGRAPHY</div>
      </div>
      <ul class="social-row">
        <li class="social-item"><span class="social-dot"></span>Facet</li>
        <li class="social-item"><span class="social-dot"></span>Prism</li>
        <li class="social-item"><span class="social-dot"></span>Warbler</li>
      </ul>
    </section>
  </main>
</body>
</html>
```